lunch promotion flyer

we recently started a new menu, would like to distribute the new menu and offer to the local office worker and residents.

Promotion Offer:
Pick any 2 delicious western Yum Cha for only $12
( Offer valid until 28/2/2015)
Updates

The flyer should contain the full menu and highlight the promotion, not just the promotion offer, it is totally wrong.

Target Market(s)

local office workers and local residents,

office workers are mainly working for the banks

Industry/Entity Type

Office

```html
<!DOCTYPE html>
<html lang="en">
<head>
<meta charset="utf-8">
<title>Quayside Kitchen – Menu</title>
<link href="https://fonts.googleapis.com/css2?family=Pathway+Gothic+One&family=Fjalla+One&family=Open+Sans:wght@600;700&display=swap" rel="stylesheet">
<style>
:root{
  --page:#e6e6e6;
  --top:#dcdcdc;
  --brand-box:#f2f2f2;
  --dark:#262626;
  --green:#245a3a;
  --orange:#ea6a2b;
  --social:#3d8a2e;
  --white:#ffffff;
}
*{margin:0;padding:0;box-sizing:border-box}
html,body{width:862px;height:1200px;overflow:hidden;background:var(--page)}
.flyer{position:relative;width:862px;height:1200px;background:var(--page);font-family:"Pathway Gothic One",sans-serif;color:var(--green)}
.top-strip{position:absolute;left:0;top:0;width:862px;height:25px;background:var(--top)}
.brand{position:absolute;left:0;top:25px;width:295px;height:122px;background:var(--brand-box);display:flex;align-items:center;justify-content:center;gap:10px}
.brand-name{font-family:"Pathway Gothic One",sans-serif;font-size:40px;color:var(--green);letter-spacing:.5px}
.brand-mark{width:18px;height:18px;border-radius:50%;background:var(--orange)}
.masthead{position:absolute;left:295px;top:25px;width:567px;height:122px;background:var(--dark)}
.tagline{position:absolute;left:0;right:0;top:33px;text-align:center;font-family:"Open Sans",sans-serif;font-weight:600;font-size:20.5px;line-height:28px;color:var(--orange)}
.social{position:absolute;left:470px;top:0;display:flex;gap:4px}
.social span{display:block;width:21px;height:28px;background:var(--social)}
.menu{position:absolute;left:26px;top:156px;width:810px}
.row{display:flex;align-items:center;height:32.3px;font-size:26.5px;line-height:1;white-space:nowrap}
.row .dish{flex:1}
.row .tag{width:60px;text-align:center;color:var(--orange)}
.row .price{width:51px;text-align:right;color:var(--orange)}
.section{font-family:"Fjalla One",sans-serif;font-size:24px;color:var(--orange);height:32.3px;display:flex;align-items:center;justify-content:space-between}
.promo{font-family:"Open Sans",sans-serif;font-weight:700;font-size:14px;color:var(--white);background:var(--orange);border-radius:14px;padding:4px 14px;line-height:18px}
.promo small{font-weight:600;font-size:11px;margin-left:6px}
.legend{justify-content:center;gap:12px;font-size:27px}
.legend b{font-family:"Open Sans",sans-serif;font-weight:700;color:var(--orange);font-size:23px}
.footer{position:absolute;left:0;top:1129px;width:862px;height:71px;background:var(--dark);display:flex;align-items:center;justify-content:center;font-family:"Open Sans",sans-serif;font-weight:600;font-size:24px;color:var(--orange)}
</style>
</head>
<body>
<div class="flyer">
  <div class="top-strip"></div>
  <div class="brand"><span class="brand-name">Quayside Kitchen</span><span class="brand-mark"></span></div>
  <div class="masthead">
    <div class="social"><span></span><span></span></div>
    <p class="tagline">Dine in or takeaway,<br>please try Quayside Kitchen healthy fresh new menu</p>
  </div>

  <div class="menu">
    <div class="section"><span>Western Yum Cha</span><span class="promo">Pick any 2 Western Yum Cha for only $12<small>(valid until 28/2/2015)</small></span></div>
    <div class="row"><span class="dish">Spanish Serrano ham &amp; cauliflower croquettes w saffron aioli</span><span class="tag"></span><span class="price">9</span></div>
    <div class="row"><span class="dish">Spicy beef meatballs w rich tomato sugo &amp; yoghurt</span><span class="tag">GF</span><span class="price">8</span></div>
    <div class="row"><span class="dish">Garlic &amp; chili prawns- pan fried&nbsp; w crusty bread</span><span class="tag"></span><span class="price">13</span></div>
    <div class="row"><span class="dish">Potato bravas – crispy fried potato w Spanish&nbsp; spicy&nbsp; tomato aioli</span><span class="tag">V/GF</span><span class="price">6</span></div>
    <div class="row"><span class="dish">Pesto arancini – Italian risotto ball&nbsp; w aioli</span><span class="tag"></span><span class="price">7</span></div>
    <div class="row"><span class="dish">Beef shaslicks – marinated porterhouse&nbsp; beef, onion &amp; capsicum</span><span class="tag"></span><span class="price">13</span></div>
    <div class="row"><span class="dish">Vegetarian rice paper rolls w hoisin dipping sauce</span><span class="tag">VG/GF</span><span class="price">7</span></div>
    <div class="row"><span class="dish">Crispy calamari – lightly fried&nbsp; w aioli &amp; lemon</span><span class="tag">GF</span><span class="price">11</span></div>
    <div class="row"><span class="dish">Bruschetta –warmed&nbsp; tomatoes , Spanish onion, basil &amp; fetta w balsamic glaze</span><span class="tag">V</span><span class="price">9</span></div>
    <div class="row"><span class="dish">Chicken drumettes , oven roasted w spicy plum sauce &amp; sesame seeds</span><span class="tag"></span><span class="price">8</span></div>
    <div class="row"><span class="dish">Sweet corn &amp; coriander&nbsp; fritters , crunchy fried fritter w guacamole</span><span class="tag">V</span><span class="price">9</span></div>
    <div class="row"><span class="dish">Sweet potato wafers , sumac salt seasoning w aioli</span><span class="tag">GF</span><span class="price">7</span></div>
    <div class="row"><span class="dish">Dips w warm Turkish pide</span><span class="tag"></span><span class="price">14</span></div>

    <div class="section"><span>Salads</span></div>
    <div class="row"><span class="dish">Cucumber, honey dew w goats cheese dressing (+ chicken)</span><span class="tag">V</span><span class="price">11 (14)</span></div>
    <div class="row"><span class="dish">Rice noodles w crispy calamari &amp; vegetables</span><span class="tag">GF</span><span class="price">13</span></div>
    <div class="row"><span class="dish">Thai beef w Asian vegetables, lemongrass and crushed nuts</span><span class="tag"></span><span class="price">13</span></div>
    <div class="row"><span class="dish">Gourmet tomato medley &amp; mixed beans w&nbsp; basil dressing</span><span class="tag">VG</span><span class="price">10</span></div>
    <div class="row"><span class="dish">Smoked salmon w tomato, Spanish onion &amp; fetta</span><span class="tag">GF</span><span class="price">12</span></div>

    <div class="section"><span>Bagels</span></div>
    <div class="row"><span class="dish">Smoked Salmon, dill cream cheese &amp; rocket</span><span class="tag"></span><span class="price">12</span></div>
    <div class="row"><span class="dish">Chicken, cranberry &amp; brie</span><span class="tag"></span><span class="price">12</span></div>
    <div class="row"><span class="dish">Prosciutto, roast capsicum, semi-dried tomato, rocket</span><span class="tag"></span><span class="price">12</span></div>

    <div class="section"><span>Something substantial &amp; classic</span></div>
    <div class="row"><span class="dish">Porterhouse steak sandwich with rocket, roast peppers, onions, cheese, dijonaise with chips</span><span class="price">17.5</span></div>
    <div class="row"><span class="dish">Classic Fish &amp; Chips, lightly fried fish with garden salad &amp; Chips</span><span class="price">17.5</span></div>
    <div class="row"><span class="dish">Chicken Parma -house-made crumbed breast,</span></div>
    <div class="row"><span class="dish">Napoli sauce, ham, topped with mozzarella cheese with chips &amp; salad</span><span class="price">17.5</span></div>
    <div class="row legend"><span><b>GF</b> = Gluten Free</span><span><b>V</b> = Vegetarian</span><span><b>VG</b> = Vegan</span></div>
  </div>

  <div class="footer">www.quaysidekitchen.com.au</div>
</div>
</body>
</html>
```